Brindle Logistics Business Card Design

We are a trucking and warehousing company. We run freight in the US manly from the Pacific NW to TX and back up the the PNW. We also do warehousing where we store, move, and distribute freight. Looking for a clean and modern design of business card. We would like to look rich and elegant. Attached is our logo.

Industry/Entity Type

Trucking Company

Contact Information for Business Card

Looking for a clean and modern design of business card. We would like to look rich and elegant.

Font styles to use
Sans Serif

Colors

Designer to choose colors to be used in the design.

Requirements
Must have
• logo but it should not dominate the card
Should not have
• logo should not dominate the card

```html
<!DOCTYPE html>
<html lang="en">
<head>
<meta charset="utf-8">
<title>Brindle Logistics Business Card</title>
<link href="https://fonts.googleapis.com/css2?family=Roboto:wght@400;500;700&display=swap" rel="stylesheet">
<style>
  :root {
    --bg: #d9d9d9;
    --paper: #ffffff;
    --blue: #1a5ea8;
    --orange: #e08a1e;
    --brown: #3a2a24;
    --ink: #3b3b3b;
  }
  * { box-sizing: border-box; margin: 0; padding: 0; }
  html, body { width: 1200px; height: 852px; overflow: hidden; }
  body {
    background: var(--bg);
    font-family: "Roboto", Arial, sans-serif;
    position: relative;
  }
  .card {
    position: absolute;
    width: 520px;
    height: 300px;
    background: var(--paper);
    border-radius: 22px;
    overflow: hidden;
    box-shadow: 0 10px 24px rgba(0,0,0,.18);
  }
  .card--front { left: 80px; top: 100px; }
  .card--back { left: 600px; top: 452px; }

  .edge-band {
    position: absolute; left: 0; right: 0; bottom: 0; height: 8px;
    display: flex;
  }
  .edge-band span:nth-child(1) { flex: 45; background: var(--blue); }
  .edge-band span:nth-child(2) { flex: 30; background: var(--orange); }
  .edge-band span:nth-child(3) { flex: 25; background: var(--brown); }

  .brand {
    position: absolute;
    display: flex; align-items: center; gap: 12px;
  }
  .brand__dot {
    width: 34px; height: 34px; border-radius: 50%;
    background: var(--blue);
  }
  .brand__name {
    font-weight: 500;
    color: var(--brown);
    letter-spacing: 1px;
    line-height: 1.1;
  }
  .card--front .brand { left: 100px; top: 92px; }
  .card--front .brand__name { font-size: 30px; }
  .card--back .brand { left: 170px; top: 52px; }
  .card--back .brand__name { font-size: 22px; }

  .front-web {
    position: absolute; left: 0; right: 0; top: 170px;
    text-align: center; font-size: 14px; color: var(--ink);
  }
  .front-rule {
    position: absolute; top: 205px; height: 3px;
  }
  .front-rule--blue { left: 150px; width: 110px; background: var(--blue); }
  .front-rule--orange { left: 260px; width: 110px; background: var(--orange); }
  .front-rule--top { left: 330px; top: 150px; width: 90px; height: 2px; background: var(--blue); }

  .person {
    position: absolute; left: 40px; top: 150px;
  }
  .person__name { font-size: 22px; font-weight: 700; color: var(--blue); }
  .person__title { font-size: 13px; color: var(--ink); margin-top: 2px; }
  .contact {
    position: absolute; left: 40px; top: 205px;
    list-style: none; font-size: 13px; color: var(--ink);
  }
  .contact li { display: flex; align-items: center; gap: 8px; height: 18px; }
  .contact svg { width: 12px; height: 12px; fill: var(--blue); flex: none; }
  .contact .no-icon { padding-left: 20px; }
</style>
</head>
<body>

<section class="card card--front" aria-label="Card front">
  <div class="brand">
    <span class="brand__dot"></span>
    <span class="brand__name">Brindle Logistics, LLC</span>
  </div>
  <div class="front-rule front-rule--top"></div>
  <p class="front-web">www.brindlelogisticsllc.com</p>
  <div class="front-rule front-rule--blue"></div>
  <div class="front-rule front-rule--orange"></div>
  <div class="edge-band"><span></span><span></span><span></span></div>
</section>

<section class="card card--back" aria-label="Card back">
  <div class="brand">
    <span class="brand__dot"></span>
    <span class="brand__name">Brindle Logistics, LLC</span>
  </div>
  <div class="person">
    <p class="person__name">Marcus Ellery</p>
    <p class="person__title">Managing Director</p>
  </div>
  <ul class="contact">
    <li><svg viewBox="0 0 12 12"><path d="M2 1h2.5l1 3-1.5 1a6 6 0 0 0 3 3l1-1.5 3 1V11a1 1 0 0 1-1 1A10 10 0 0 1 1 2a1 1 0 0 1 1-1z"/></svg>555 0142 3867</li>
    <li><svg viewBox="0 0 12 12"><path d="M0 2h12v8H0z M0 2l6 5 6-5" stroke="#fff" stroke-width="1"/></svg>marcus@brindlelogisticsllc.com</li>
    <li><svg viewBox="0 0 12 12"><circle cx="6" cy="6" r="5.5"/><path d="M0.5 6h11M6 .5v11" stroke="#fff" stroke-width="1"/></svg>www.brindlelogisticsllc.com</li>
    <li class="no-icon">2710 Harbor View Road, Tacoma, WA 98421</li>
  </ul>
  <div class="edge-band"><span></span><span></span><span></span></div>
</section>

</body>
</html>
```